Medical Device - Case Study Template

We need a TEMPLATE that we can reuse to write various case studies about the medical equipment solutions we provide. It will be a double sided letter sized with a modern design that conveys a feeling of expertise, innovation and highly personable service AND be consistent with the brand guide. The content will be divided into a few sections:

- Situation (200-250 words)
- Challenge (100-120 words)
- Solution (100-120 words)
- Results (100-120 words)
- Conclusion (100-120 words)

Additionally, there will need to be a call to action, inviting people to send an email for more information and a short "About Talvo" section (approx. 40 words).

For device picture placeholders, feel free to use any random small benchtop medical device.

```html
<!DOCTYPE html>
<html lang="en">
<head>
<meta charset="utf-8">
<title>Talvo – Medical Equipment Solutions Case Study</title>
<link rel="stylesheet" href="https://fonts.googleapis.com/css2?family=Oswald:wght@600;700&family=Ubuntu:wght@400;500;700&display=swap">
<style>
  :root{
    --navy:#1b3a8c;
    --navy-deep:#132d6e;
    --blue:#2a5fb0;
    --sky:#5b8cc8;
    --steel:#8eaccb;
    --pale:#d8e3ee;
    --orange:#f07f2a;
    --green:#8dc63f;
    --ink:#2b2b2b;
    --white:#ffffff;
    --backdrop:#dcdcdc;
  }
  *{box-sizing:border-box;margin:0;padding:0}
  html,body{width:1200px;height:1200px;overflow:hidden}
  body{background:var(--backdrop);font-family:"Ubuntu",sans-serif;color:var(--ink);position:relative}
  .page{position:absolute;top:242px;width:544px;height:707px;background:var(--white);overflow:hidden;box-shadow:0 1px 4px rgba(0,0,0,.25)}
  .page--front{left:44px}
  .page--back{left:609px}
  .abs{position:absolute}
  .body-copy{font-size:9.2px;line-height:11.1px;text-align:justify}
  .body-copy p+p{margin-top:7px}

  /* brand */
  .brand{display:flex;align-items:center;gap:10px}
  .brand__mark{width:26px;height:26px;background:var(--orange)}
  .brand__name{font-family:"Ubuntu",sans-serif;font-weight:500;font-size:30px;color:var(--sky);letter-spacing:1px}
  .brand--light .brand__mark{background:var(--white)}
  .brand--light .brand__name{color:var(--white);font-size:26px}

  /* headline */
  .headline{font-family:"Oswald",sans-serif;font-weight:700;font-size:41px;line-height:40px;color:var(--navy);transform:scaleX(.86);transform-origin:left}
  .headline span{display:block}
  .headline .accent{color:var(--orange)}
  .intro{font-size:9.6px;line-height:11.3px;font-weight:500;color:var(--sky)}

  /* section tabs */
  .tab{position:absolute;height:27px;display:flex;align-items:center;color:var(--white);font-size:18px;font-weight:500;letter-spacing:4px}
  .tab::before{content:"";border-left:7px solid currentColor;border-top:5px solid transparent;border-bottom:5px solid transparent;margin-right:7px}
  .tab--orange-text{color:var(--orange)}

  .challenge-copy{color:var(--white)}
  .solution-copy{color:var(--white)}

  .footer-cta{font-size:15px;letter-spacing:3px;color:var(--white);font-weight:500}
  .email{display:flex;height:24px;border-radius:12px;overflow:hidden;font-size:12px;color:var(--white)}
  .email__icon{width:38px;background:#b9c6d6;display:flex;align-items:center;justify-content:center}
  .email__text{flex:1;background:var(--orange);display:flex;align-items:center;padding-left:12px}
</style>
</head>
<body>

<!-- FRONT PAGE -->
<section class="page page--front">
  <svg class="abs" style="left:0;top:0" width="544" height="707" viewBox="0 0 544 707">
    <polygon points="0,240 250,240 272,296 250,354 0,354" fill="var(--pale)"/>
    <polygon points="262,0 544,0 544,222 518,251 300,251 218,136" fill="var(--blue)"/>
    <polygon points="300,0 544,0 544,200 516,226 318,226 262,122" fill="#7fb0e0" role="img" aria-label="Photo: hand holding floating medical devices and health icons"/>
    <line x1="17" y1="227" x2="183" y2="227" stroke="var(--green)" stroke-width="1.5"/>
    <circle cx="185" cy="227" r="2.5" fill="var(--green)"/>
    <!-- situation tab -->
    <polygon points="318,327 330,327 318,355 306,355" fill="var(--navy)"/>
    <polygon points="334,327 544,327 544,355 322,355" fill="var(--orange)"/>
    <!-- challenge band -->
    <rect x="0" y="572" width="544" height="135" fill="var(--steel)"/>
    <polygon points="0,548 206,548 218,572 0,572" fill="var(--navy)"/>
    <polygon points="206,548 212,548 224,572 218,572" fill="var(--orange)"/>
    <polygon points="544,610 544,707 482,707" fill="var(--navy)"/>
    <polygon points="544,600 544,610 478,707 470,707" fill="var(--orange)"/>
  </svg>

  <div class="brand abs" style="left:17px;top:28px"><span class="brand__mark"></span><span class="brand__name">Talvo</span></div>

  <h1 class="headline abs" style="left:17px;top:99px"><span>MEDICAL</span><span>EQUIPMENT</span><span class="accent">SOLUTIONS</span></h1>

  <p class="intro abs" style="left:17px;top:236px;width:200px">Lorem ipsum dolor sit amet, consectetur adipiscing elit. Sed volutpat pretium pharetra. Maecenas porta diam justo, vitae hendrerit nisi commodo et. Quisque eu metus condimentum, suscipit augue nec, hendrerit enim. Fusce vitae fringilla nisi, ultrices congue urna. In porttitor lacinia.</p>

  <div class="tab" style="left:358px;top:328px">SITUATION</div>

  <div class="body-copy abs" style="left:17px;top:375px;width:510px">
    <p>Lorem ipsum dolor sit amet, consectetur adipiscing elit. Sed volutpat pretium pharetra. Maecenas porta diam justo, vitae hendrerit nisi commodo et. Quisque eu metus condimentum, suscipit augue nec, hendrerit enim. Fusce vitae fringilla nisi, ultrices congue urna. In porttitor lacinia mi at accumsan. Donec pharetra mi a sem cursus congue. Curabitur suscipit consectetur dolor, sed rhoncus diam porta vel. Sed consequat egestas bibendum. Proin nec ex est. Phasellus rutrum, libero eu consequat semper, felis libero vestibulum odio, sit amet dignissim nulla tortor at urna. Nunc dignissim ullamcorper urna, non vulputate dolor interdum sed. Sed laoreet tempor lectus, dapibus ornare tellus commodo ac. Praesent faucibus tincidunt faucibus. Suspendisse tristique, nisl sit amet sollicitudin laoreet, orci felis scelerisque lectus, ut lobortis tellus est sed eros. In hac habitasse platea dictumst. Praesent enim quam, tincidunt pellentesque mauris in, imperdiet lobortis magna. Praesent non blandit leo. Morbi et quam felis.</p>
    <p>Mauris scelerisque ex sit amet pretium lobortis. In hac habitasse platea dictumst. Mauris posuere enim vel ante dignissim, eleifend accumsan justo pulvinar. Nam ullamcorper ex sapien, non pharetra nunc dapibus ut. Nam dignissim, odio quis tempus pellentesque, sem libero maximus tellus, interdum lacinia enim massa nec nibh. Mauris pretium semper dictum. Suspendisse accumsan tincidunt tellus, vel egestas ligula tempor sit amet. Pellentesque tristique nunc in dui eleifend, in varius ipsum tempor. Mauris feugiat diam ut augue condimentum, sodales pulvinar eros.</p>
  </div>

  <div class="tab" style="left:8px;top:547px;font-size:19px">CHALLENGE</div>

  <div class="body-copy challenge-copy abs" style="left:14px;top:588px;width:500px">
    <p>Lorem ipsum dolor sit amet, consectetur adipiscing elit. Sed volutpat pretium pharetra. Maecenas porta diam justo, vitae hendrerit nisi commodo et. Quisque eu metus condimentum, suscipit augue nec, hendrerit enim. Fusce vitae fringilla nisi, ultrices congue urna. In porttitor lacinia mi at accumsan. Donec pharetra mi a sem cursus congue. Curabitur suscipit consectetur dolor, sed rhoncus diam porta vel. Sed consequat egestas bibendum. Proin nec ex est. Phasellus rutrum, libero eu consequat semper, felis libero vestibulum odio, sit amet dignissim nulla tortor at urna. Nunc dignissim ullamcorper urna, non vulputate dolor interdum sed. Sed laoreet tempor lectus, dapibus ornare tellus commodo ac. Praesent faucibus tincidunt faucibus. Suspendisse tristique, nisl sit amet sollicitudin laoreet, orci felis scelerisque lectus, ut lobortis tellus est sed eros.</p>
  </div>
</section>

<!-- BACK PAGE -->
<section class="page page--back">
  <svg class="abs" style="left:0;top:0" width="544" height="707" viewBox="0 0 544 707">
    <defs>
      <linearGradient id="solutionBg" x1="0" y1="0" x2="1" y2="0">
        <stop offset="0" stop-color="var(--navy-deep)"/><stop offset="1" stop-color="var(--blue)"/>
      </linearGradient>
      <linearGradient id="backFade" x1="0" y1="0" x2="0" y2="1">
        <stop offset="0" stop-color="#ffffff"/><stop offset="1" stop-color="#dfe8f2"/>
      </linearGradient>
    </defs>
    <rect width="544" height="707" fill="url(#backFade)"/>
    <rect width="544" height="200" fill="url(#solutionBg)"/>
    <polygon points="133,0 378,0 362,28 146,28" fill="var(--green)"/>
    <!-- hex photos -->
    <polygon points="432,10 508,10 546,74 508,138 432,138 394,74" fill="#9fb3c8"/>
    <polygon points="440,22 500,22 532,74 500,126 440,126 408,74" fill="#6f8aa6" role="img" aria-label="Photo: close-up of microscope objective lenses"/>
    <polygon points="432,142 508,142 546,206 508,270 432,270 394,206" fill="var(--green)"/>
    <polygon points="440,154 500,154 532,206 500,258 440,258 408,206" fill="#7d93ad" role="img" aria-label="Photo: laboratory microscope"/>
    <!-- results illustration -->
    <polygon points="322,232 410,232 450,352 410,472 322,472 282,352" fill="#eef3f8" role="img" aria-label="Illustration: ring of line icons for healthcare, logistics and analytics"/>
    <polygon points="330,285 402,285 432,346 402,407 330,407 300,346" fill="#9fb3c8"/>
    <polygon points="338,297 394,297 418,346 394,395 338,395 314,346" fill="#5f7896" role="img" aria-label="Photo: benchtop medical analyser"/>
    <!-- conclusion -->
    <polygon points="18,471 250,471 262,498 18,498" fill="var(--orange)"/>
    <polygon points="252,471 258,471 270,498 264,498" fill="var(--navy)"/>
    <rect x="18.5" y="498.5" width="509" height="121" fill="var(--white)" stroke="var(--orange)"/>
    <!-- footer -->
    <polygon points="0,640 480,640 505,707 0,707" fill="var(--navy)"/>
    <polygon points="486,640 496,640 521,673 496,707 486,707 511,673" fill="var(--orange)"/>
    <polygon points="500,640 510,640 535,673 510,707 500,707 525,673" fill="var(--navy)"/>
  </svg>

  <div class="tab" style="left:168px;top:1px;letter-spacing:4px">SOLUTION</div>

  <div class="body-copy solution-copy abs" style="left:18px;top:49px;width:362px">
    <p>Lorem ipsum dolor sit amet, consectetur adipiscing elit. Sed volutpat pretium pharetra. Maecenas porta diam justo, vitae hendrerit nisi commodo et. Quisque eu metus condimentum, suscipit augue nec, hendrerit enim. Fusce vitae fringilla nisi, ultrices congue urna. In porttitor lacinia mi at accumsan. Donec pharetra mi a sem cursus congue. Curabitur suscipit consectetur dolor, sed rhoncus diam porta vel. Sed consequat egestas bibendum. Proin nec ex est. Phasellus rutrum, libero eu consequat semper, felis libero vestibulum odio, sit amet dignissim nulla tortor at urna. Nunc dignissim ullamcorper urna, non vulputate dolor interdum sed. Sed laoreet tempor lectus, dapibus ornare tellus commodo ac. Praesent faucibus tincidunt faucibus. Suspendisse tristique, nisl sit amet sollicitudin laoreet, orci felis scelerisque lectus, ut lobortis tellus est sed eros.</p>
  </div>

  <div class="tab tab--orange-text" style="left:58px;top:215px">RESULTS</div>

  <div class="body-copy abs" style="left:16px;top:250px;width:228px">
    <p>Lorem ipsum dolor sit amet, consectetur adipiscing elit. Sed volutpat pretium pharetra. Maecenas porta diam justo, vitae hendrerit nisi commodo et. Quisque eu metus condimentum, suscipit augue nec, hendrerit enim. Fusce vitae fringilla nisi, ultrices congue urna. In porttitor lacinia mi at accumsan. Donec pharetra mi a sem cursus congue. Curabitur suscipit consectetur dolor, sed rhoncus diam porta vel. Sed consequat egestas bibendum. Proin nec ex est. Phasellus rutrum, libero eu consequat semper, felis libero vestibulum odio, sit amet dignissim nulla tortor at urna. Nunc dignissim ullamcorper urna, non vulputate dolor interdum sed. Sed laoreet tempor lectus, dapibus ornare tellus commodo ac. Praesent faucibus tincidunt faucibus. Suspendisse tristique, nisl sit amet sollicitudin laoreet, orci felis scelerisque lectus, ut lobortis tellus est sed eros.</p>
  </div>

  <div class="tab" style="left:26px;top:471px;font-size:19px">CONCLUSION</div>

  <div class="body-copy abs" style="left:34px;top:512px;width:478px">
    <p>Lorem ipsum dolor sit amet, consectetur adipiscing elit. Sed volutpat pretium pharetra. Maecenas porta diam justo, vitae hendrerit nisi commodo et. Quisque eu metus condimentum, suscipit augue nec, hendrerit enim. Fusce vitae fringilla nisi, ultrices congue urna. In porttitor lacinia mi at accumsan. Donec pharetra mi a sem cursus congue. Curabitur suscipit consectetur dolor, sed rhoncus diam porta vel. Sed consequat egestas bibendum. Proin nec ex est. Phasellus rutrum, libero eu consequat semper, felis libero vestibulum odio, sit amet dignissim nulla tortor at urna. Nunc dignissim ullamcorper urna, non vulputate dolor interdum sed. Sed laoreet tempor lectus, dapibus ornare tellus commodo ac. Praesent faucibus tincidunt faucibus. Suspendisse tristique, nisl sit amet sollicitudin laoreet, orci felis scelerisque lectus, ut lobortis tellus est sed eros.</p>
  </div>

  <div class="brand brand--light abs" style="left:22px;top:659px"><span class="brand__mark"></span><span class="brand__name">Talvo</span></div>

  <div class="footer-cta abs" style="left:264px;top:651px">FOR MORE INFO:</div>

  <div class="email abs" style="left:220px;top:673px;width:238px">
    <span class="email__icon">
      <svg width="16" height="11" viewBox="0 0 16 11"><rect x="0.5" y="0.5" width="15" height="10" fill="none" stroke="#4a5d78"/><polyline points="0.5,0.5 8,6 15.5,0.5" fill="none" stroke="#4a5d78"/></svg>
    </span>
    <span class="email__text">info@talvomedicaltech.com</span>
  </div>
</section>

</body>
</html>
```